Proposal & Presentation Slides

We need power point slides template to build proposal for prospects. slides should include: We provide prospect two items, presentation and proposal. We need power point slide design that can be used for both. One of the following option will work:
So we can include 1-2 slides in proposal to demonstrate service included
or
we can use power power slides and last 1-2 slides will have page for them to sign off.

Target Market(s)

It varies: we are IT Management Firm and provide servies to many different companies in Canada

Industry/Entity Type

Business Consultant

Font styles to use
Serif

Colors

Designer to choose colors to be used in the design.

Requirements
Must have
• Information about our company
• About Tidewell Process
• Proposal sign off form
• Colors : we had logo design project on sketchmarket, please use all logos and colors accordingly

```html
<!DOCTYPE html>
<html lang="en">
<head>
<meta charset="utf-8">
<title>Tidewell Systems Group – Slide Template</title>
<link href="https://fonts.googleapis.com/css2?family=Open+Sans:wght@400;600;700;800&family=Merriweather:wght@300;400;700&display=swap" rel="stylesheet">
<style>
:root{
  --red:#b3191f;
  --red-dark:#7d1015;
  --red-deep:#4a0a0d;
  --ink:#333;
  --grey:#6d6d6d;
  --grey-light:#d9d9d9;
  --paper:#fff;
  --bg:#eeeeee;
  --gold:#e0a12a;
  --orange:#d9662b;
  --photo-cool:linear-gradient(135deg,#8d9aa6,#c9ced3);
  --photo-warm:linear-gradient(135deg,#6b4a3c,#b9a08e);
  --photo-dark:linear-gradient(135deg,#2b2b2b,#6a1014);
}
*{box-sizing:border-box;margin:0;padding:0}
html,body{width:774px;height:1200px;overflow:hidden}
body{background:var(--bg);font-family:"Open Sans",Arial,sans-serif;color:var(--ink);position:relative}

.brand-header{position:absolute;left:16px;top:18px;width:480px;height:125px}
.brand-name{display:flex;align-items:center;gap:12px;font-family:"Open Sans",Arial,sans-serif;font-weight:700;font-size:40px;color:var(--ink);line-height:1.1}
.brand-dot{width:30px;height:30px;border-radius:50%;background:var(--red);flex:none}
.brand-tag{font-family:"Merriweather",Georgia,serif;font-weight:400;font-size:17px;color:var(--grey);margin-top:14px}
.brand-rule{width:120px;height:4px;background:var(--red);margin-top:14px}

.hero-slide{position:absolute;left:508px;top:22px;width:240px;height:122px}

.slide-grid{position:absolute;left:13px;top:160px;width:748px;display:grid;grid-template-columns:repeat(3,1fr);grid-auto-rows:140px;gap:9px 12px}
.slide{position:relative;background:var(--paper);overflow:hidden;font-size:6px;line-height:1.35;box-shadow:0 1px 3px rgba(0,0,0,.25)}
.slide h3{position:absolute;font-family:"Merriweather",Georgia,serif;font-size:10px;font-weight:700;color:var(--ink)}
.abs{position:absolute}
.photo{position:absolute}
.photo.cool{background:var(--photo-cool)}
.photo.warm{background:var(--photo-warm)}
.photo.dark{background:var(--photo-dark)}
.red{background:var(--red)}
.redd{background:var(--red-dark)}
.line{position:absolute;height:2px;background:var(--grey-light)}
.footer-bar{position:absolute;left:0;right:0;bottom:0;height:4px;background:var(--red)}
.small-text{color:var(--grey);font-size:5px}
.white{color:#fff}

.title-slide{background:var(--red-deep)}
.title-slide .glow{position:absolute;inset:0;background:radial-gradient(circle at 35% 50%,#b3191f 0%,#4a0a0d 60%,#1c0405 100%)}
.title-name{position:absolute;left:50%;top:30%;font-family:"Merriweather",Georgia,serif;font-weight:700;font-size:15px;color:#fff;letter-spacing:1px}
.title-sub{position:absolute;left:50%;top:46%;font-size:6px;color:#fff}
.title-main{position:absolute;left:50%;top:60%;font-size:9px;font-weight:700;color:#fff}
.title-date{position:absolute;left:50%;top:70%;font-size:5px;color:#f3d0d0}

.toc-panel{position:absolute;left:0;top:0;bottom:0;width:42%;background:var(--red-dark)}
.toc-row{position:absolute;left:46%;right:6%;height:18px;display:flex;gap:5px;align-items:center}
.toc-num{width:14px;height:14px;background:var(--red);color:#fff;font-size:6px;font-weight:700;display:flex;align-items:center;justify-content:center}
.btn{position:absolute;background:var(--red);color:#fff;font-size:5px;font-weight:700;text-align:center;line-height:11px;height:11px}
.icon-box{position:absolute;width:26px;height:26px;background:var(--red);border-radius:3px}
.card{position:absolute;top:40px;width:52px;height:84px;color:#fff;padding:4px;font-size:5px}
</style>
</head>
<body>

<header class="brand-header">
  <div class="brand-name"><span class="brand-dot"></span><span>Tidewell Systems Group</span></div>
  <div class="brand-tag">Managed IT, planned with care for every team</div>
  <div class="brand-rule"></div>
</header>

<div class="slide hero-slide title-slide">
  <div class="glow"></div>
  <div class="title-name" style="left:52%;top:24%">TIDEWELL</div>
  <div class="title-sub" style="left:52%;top:40%">Systems Group</div>
  <div class="title-main" style="left:52%;top:58%">PRESENTATION TITLE</div>
  <div class="title-date" style="left:52%;top:70%">Sub title goes here</div>
</div>

<main class="slide-grid">

  <section class="slide">
    <div class="abs red" style="left:0;top:0;width:10px;height:100%"></div>
    <div class="abs" style="left:22px;top:22px;font-weight:800;font-size:13px;color:#1f4e8c">Northmere</div>
    <div class="abs small-text" style="left:22px;top:42px">Prepared for our valued client</div>
    <div class="photo cool" role="img" aria-label="Photo of a business team in an office" style="left:46%;top:12%;width:54%;height:70%"></div>
    <div class="abs red" style="left:46%;top:82%;width:54%;height:8px"></div>
  </section>

  <section class="slide title-slide">
    <div class="glow"></div>
    <div class="title-name">TIDEWELL</div>
    <div class="title-sub">Systems Group</div>
    <div class="title-main">PRESENTATION TITLE</div>
    <div class="title-date">Sub title goes here</div>
  </section>

  <section class="slide">
    <h3 style="left:10px;top:8px">Sign - Off</h3>
    <div class="abs small-text" style="left:10px;top:28px">Client Name</div>
    <div class="line" style="left:10px;top:36px;width:100px"></div>
    <div class="abs small-text" style="left:10px;top:44px">Signature</div>
    <div class="line" style="left:10px;top:52px;width:100px"></div>
    <div class="abs small-text" style="left:10px;top:60px">Title</div>
    <div class="line" style="left:10px;top:68px;width:100px"></div>
    <div class="abs small-text" style="left:10px;top:76px">Date</div>
    <div class="line" style="left:10px;top:84px;width:100px"></div>
    <div class="photo warm" role="img" aria-label="Photo of hands signing a document" style="left:58%;top:14%;width:42%;height:72%"></div>
    <div class="footer-bar"></div>
  </section>

  <section class="slide">
    <div class="toc-panel"></div>
    <div class="abs white" style="left:10px;top:56px;font-family:Merriweather,serif;font-size:11px;font-weight:700;width:80px">Table of contents</div>
    <div class="toc-row" style="top:14px"><span class="toc-num">01</span><span>Contents title here</span></div>
    <div class="toc-row" style="top:38px"><span class="toc-num">02</span><span>Contents title here</span></div>
    <div class="toc-row" style="top:62px"><span class="toc-num">03</span><span>Contents title here</span></div>
    <div class="toc-row" style="top:86px"><span class="toc-num">04</span><span>Contents title here</span></div>
    <div class="toc-row" style="top:110px"><span class="toc-num">05</span><span>Contents title here</span></div>
  </section>

  <section class="slide">
    <h3 style="left:10px;top:8px">About our company</h3>
    <div class="photo cool" role="img" aria-label="Photo of a meeting room" style="left:10px;top:30px;width:44%;height:80px"></div>
    <div class="abs red" style="left:58%;top:30px;width:38%;height:26px"></div>
    <div class="abs small-text" style="left:58%;top:62px;width:38%">We manage IT for growing companies across Canada with care.</div>
    <div class="abs redd" style="left:58%;top:90px;width:38%;height:20px"></div>
    <div class="footer-bar"></div>
  </section>

  <section class="slide">
    <h3 style="left:10px;top:8px">Total Technology Cost</h3>
    <div class="btn" style="left:30px;top:32px;width:60px">ONE TIME</div>
    <div class="btn" style="left:140px;top:32px;width:60px">MONTHLY</div>
    <div class="line" style="left:20px;top:56px;width:200px"></div>
    <div class="line" style="left:20px;top:70px;width:200px"></div>
    <div class="line" style="left:20px;top:84px;width:200px"></div>
    <div class="line" style="left:20px;top:98px;width:200px"></div>
    <div class="abs red" style="left:20px;top:110px;width:200px;height:10px"></div>
  </section>

  <section class="slide">
    <h3 style="left:10px;top:8px">Business requirements - IT</h3>
    <svg class="abs" style="left:20px;top:34px" width="120" height="90" viewBox="0 0 120 90">
      <ellipse cx="60" cy="52" rx="52" ry="26" fill="#7d1015"/>
      <path d="M60 45 L60 19 A52 26 0 0 1 111 40 Z" fill="#b3191f"/>
      <path d="M60 45 L111 40 A52 26 0 0 1 70 70 Z" fill="#999"/>
      <path d="M60 45 L70 70 A52 26 0 0 1 9 48 Z" fill="#c9c9c9"/>
      <path d="M60 45 L9 48 A52 26 0 0 1 60 19 Z" fill="#d9662b"/>
    </svg>
    <div class="abs small-text" style="left:150px;top:40px;width:80px">Network<br>Security<br>Cloud<br>Backup<br>Support</div>
  </section>

  <section class="slide">
    <h3 style="left:10px;top:8px">Tidewell Way - Process</h3>
    <div class="abs red" style="left:10px;top:34px;width:68px;height:24px"></div>
    <div class="abs redd" style="left:86px;top:34px;width:68px;height:24px"></div>
    <div class="abs red" style="left:162px;top:34px;width:68px;height:24px"></div>
    <div class="abs small-text" style="left:10px;top:64px;width:68px">Assess your current systems</div>
    <div class="abs small-text" style="left:86px;top:64px;width:68px">Plan the right solution</div>
    <div class="abs small-text" style="left:162px;top:64px;width:68px">Manage and support daily</div>
    <div class="abs" style="left:10px;top:96px;width:220px;height:28px;background:#f1f1f1"></div>
  </section>

  <section class="slide">
    <svg class="abs" style="left:0;top:0" width="241" height="140" viewBox="0 0 241 140">
      <circle cx="120" cy="70" r="40" fill="none" stroke="#ddd" stroke-width="2"/>
      <circle cx="120" cy="70" r="18" fill="#b3191f"/>
      <text x="120" y="72" font-size="6" font-family="Open Sans,sans-serif" font-weight="700" fill="#fff" text-anchor="middle">SERVICE</text>
      <circle cx="120" cy="30" r="9" fill="#7d1015"/><circle cx="155" cy="50" r="9" fill="#d9662b"/>
      <circle cx="155" cy="90" r="9" fill="#b3191f"/><circle cx="120" cy="110" r="9" fill="#7d1015"/>
      <circle cx="85" cy="90" r="9" fill="#d9662b"/><circle cx="85" cy="50" r="9" fill="#b3191f"/>
    </svg>
    <div class="abs small-text" style="left:8px;top:20px;width:60px">Lorem ipsum dolor</div>
    <div class="abs small-text" style="left:180px;top:20px;width:56px">Lorem ipsum dolor</div>
    <div class="abs small-text" style="left:8px;top:110px;width:60px">Lorem ipsum dolor</div>
    <div class="abs small-text" style="left:180px;top:110px;width:56px">Lorem ipsum dolor</div>
  </section>

  <section class="slide">
    <h3 style="left:10px;top:8px">Our Service</h3>
    <div class="icon-box" style="left:20px;top:40px"></div>
    <div class="icon-box" style="left:76px;top:40px"></div>
    <div class="icon-box" style="left:132px;top:40px"></div>
    <div class="icon-box" style="left:188px;top:40px"></div>
    <div class="abs small-text" style="left:14px;top:74px;width:220px">Help desk · Network · Cloud · Security</div>
    <div class="abs red" style="left:0;top:100px;width:100%;height:40px"></div>
  </section>

  <section class="slide">
    <h3 style="left:10px;top:8px">Lorem ipsum consectetur</h3>
    <div class="card" style="left:8px;background:#a35a2e">Plan</div>
    <div class="card" style="left:65px;background:var(--gold)">Build</div>
    <div class="card" style="left:122px;background:var(--orange)">Run</div>
    <div class="card" style="left:179px;background:var(--red)">Grow</div>
  </section>

  <section class="slide">
    <div class="abs" style="left:10px;top:14px;font-family:Merriweather,serif;font-size:8px;font-weight:700;width:100px;color:var(--red)">Lorem ipsum dolor sit amet lift at dolor</div>
    <div class="abs small-text" style="left:10px;top:48px;width:100px">Short note about the service and its value for clients.</div>
    <div class="photo cool" role="img" aria-label="Photo of a laptop on a desk" style="left:52%;top:12px;width:44%;height:84px"></div>
    <div class="abs red" style="left:0;top:110px;width:100%;height:30px"></div>
  </section>

  <section class="slide">
    <div class="photo warm" role="img" aria-label="Photo of a smiling client" style="left:0;top:0;width:38%;height:100%"></div>
    <div class="abs" style="left:44%;top:10px;font-family:Merriweather,serif;font-size:8px;font-weight:700">Lorem ipsum dolor sit amet</div>
    <svg class="abs" style="left:44%;top:32px" width="12" height="96" viewBox="0 0 12 96">
      <circle cx="6" cy="6" r="5" fill="#b3191f"/><circle cx="6" cy="30" r="5" fill="#b3191f"/>
      <circle cx="6" cy="54" r="5" fill="#b3191f"/><circle cx="6" cy="78" r="5" fill="#b3191f"/>
    </svg>
    <div class="abs small-text" style="left:52%;top:32px;width:44%;line-height:24px">Lorem ipsum dolor<br>Lorem ipsum dolor<br>Lorem ipsum dolor<br>Lorem ipsum dolor</div>
  </section>

  <section class="slide">
    <div class="photo warm" role="img" aria-label="Photo of colleagues working together" style="left:0;top:0;width:100%;height:100%"></div>
    <div class="abs" style="left:8%;top:20%;font-family:Merriweather,serif;font-size:11px;font-weight:700;color:#fff">About our company</div>
    <div class="abs" style="left:60%;top:0;width:40%;height:100%;background:rgba(255,255,255,.9)"></div>
    <div class="abs small-text" style="left:63%;top:20%;width:34%">We keep your technology running so your team can focus on growth.</div>
  </section>

  <section class="slide">
    <h3 style="left:10px;top:8px">Lorem ipsum consectetur</h3>
    <div class="abs red" style="left:10px;top:30px;width:220px;height:10px"></div>
    <div class="line" style="left:10px;top:50px;width:220px"></div>
    <div class="line" style="left:10px;top:64px;width:220px"></div>
    <div class="line" style="left:10px;top:78px;width:220px"></div>
    <div class="line" style="left:10px;top:92px;width:220px"></div>
    <div class="abs red" style="left:80px;top:46px;width:60px;height:6px"></div>
    <div class="abs redd" style="left:120px;top:60px;width:70px;height:6px"></div>
    <div class="abs red" style="left:160px;top:74px;width:50px;height:6px"></div>
    <div class="abs redd" style="left:100px;top:88px;width:90px;height:6px"></div>
  </section>

  <section class="slide">
    <h3 style="left:10px;top:8px">Lorem ipsum consectetur</h3>
    <svg class="abs" style="left:10px;top:32px" width="220" height="100" viewBox="0 0 220 100">
      <circle cx="110" cy="50" r="34" fill="none" stroke="#b3191f" stroke-width="3"/>
      <circle cx="30" cy="22" r="12" fill="#b3191f"/><circle cx="30" cy="78" r="12" fill="#7d1015"/>
      <circle cx="190" cy="22" r="12" fill="#7d1015"/><circle cx="190" cy="78" r="12" fill="#b3191f"/>
      <text x="110" y="53" font-size="8" font-family="Open Sans,sans-serif" text-anchor="middle" fill="#333">Content Here</text>
    </svg>
  </section>

  <section class="slide">
    <div class="abs red" style="left:0;top:0;width:100%;height:34px"></div>
    <div class="abs white" style="left:10px;top:11px;font-family:Merriweather,serif;font-size:9px;font-weight:700">Lorem ipsum consectetur</div>
    <div class="photo cool" role="img" aria-label="Photo of an office desk with devices" style="left:10px;top:44px;width:45%;height:84px"></div>
    <div class="abs small-text" style="left:58%;top:48px;width:38%">Short summary of our managed services and the results clients see.</div>
  </section>

  <section class="slide">
    <div class="photo dark" role="img" aria-label="Photo of a person using a phone" style="left:0;top:0;width:100%;height:100%"></div>
    <div class="abs white" style="left:55%;top:22px;font-family:Merriweather,serif;font-size:12px;font-weight:700">Get in Touch</div>
    <svg class="abs" style="left:55%;top:48px" width="10" height="60" viewBox="0 0 10 60">
      <circle cx="5" cy="5" r="5" fill="#b3191f"/><circle cx="5" cy="27" r="5" fill="#b3191f"/><circle cx="5" cy="49" r="5" fill="#b3191f"/>
    </svg>
    <div class="abs white" style="left:62%;top:47px;font-size:5px;line-height:22px">+1 555 010 2040<br>info@tidewell.example<br>12 Harbour St, Halifax</div>
  </section>

  <section class="slide">
    <div class="photo dark" role="img" aria-label="Photo of a dark office interior" style="left:0;top:0;width:100%;height:100%"></div>
    <div class="abs white" style="left:0;right:0;top:58px;text-align:center;font-family:Merriweather,serif;font-size:13px;font-weight:700;letter-spacing:2px">PROPOSAL</div>
  </section>

  <section class="slide">
    <h3 style="left:10px;top:8px">Proposal</h3>
    <svg class="abs" style="left:20px;top:34px" width="200" height="96" viewBox="0 0 200 96">
      <line x1="0" y1="92" x2="200" y2="92" stroke="#ccc"/>
      <rect x="10" y="40" width="14" height="52" fill="#d9662b"/><rect x="26" y="20" width="14" height="72" fill="#b3191f"/>
      <rect x="60" y="50" width="14" height="42" fill="#d9662b"/><rect x="76" y="30" width="14" height="62" fill="#b3191f"/>
      <rect x="110" y="35" width="14" height="57" fill="#d9662b"/><rect x="126" y="10" width="14" height="82" fill="#b3191f"/>
      <rect x="160" y="55" width="14" height="37" fill="#d9662b"/><rect x="176" y="25" width="14" height="67" fill="#b3191f"/>
    </svg>
  </section>

  <section class="slide">
    <h3 style="left:10px;top:8px">Proposal</h3>
    <svg class="abs" style="left:20px;top:34px" width="200" height="96" viewBox="0 0 200 96">
      <path d="M40 48 H160" stroke="#ddd" stroke-width="2"/>
      <circle cx="40" cy="48" r="18" fill="none" stroke="#b3191f" stroke-width="3"/>
      <circle cx="100" cy="48" r="18" fill="none" stroke="#d9662b" stroke-width="3"/>
      <circle cx="160" cy="48" r="18" fill="none" stroke="#7d1015" stroke-width="3"/>
      <text x="40" y="51" font-size="8" text-anchor="middle" font-family="Open Sans,sans-serif" fill="#333">01</text>
      <text x="100" y="51" font-size="8" text-anchor="middle" font-family="Open Sans,sans-serif" fill="#333">02</text>
      <text x="160" y="51" font-size="8" text-anchor="middle" font-family="Open Sans,sans-serif" fill="#333">03</text>
    </svg>
  </section>

</main>
</body>
</html>
```